Looking for a professional, clean and crisp business card

I am in the underground utilities industry and am just looking for a really impressive business card. I would like our card to be white with our symbol crisp and clear with it protruding. I also have a business partner that will require his name and info on the card once the design is set. I would like to have our website info on the card which is;
http://granitetrenchco.example/

Contact Information for Business Card

Website, contact name, number and email

```html
<!DOCTYPE html>
<html lang="en">
<head>
<meta charset="utf-8">
<title>Granite Trench Co — Business Card</title>
<link rel="stylesheet" href="https://fonts.googleapis.com/css2?family=Lato:wght@400;700;900&display=swap">
<style>
  :root {
    --backdrop: #3a3b3e;
    --card-black: #0b0b0b;
    --card-white: #ffffff;
    --brand-blue: #3b5fa8;
    --text-dark: #111111;
    --text-muted: #555555;
    --text-light: #f4f4f4;
  }
  * { box-sizing: border-box; margin: 0; padding: 0; }
  html, body {
    width: 1200px; height: 900px; overflow: hidden;
    background: var(--backdrop);
    font-family: "Lato", sans-serif;
  }
  .sheet {
    width: 1200px; height: 900px;
    display: flex; flex-direction: column;
    align-items: center; justify-content: center; gap: 40px;
  }
  .card {
    position: relative;
    width: 640px; height: 366px;
    border-radius: 28px;
    overflow: hidden;
  }
  .card--back {
    background: var(--card-black);
    display: flex; align-items: center; justify-content: center;
  }
  .wordmark {
    display: flex; align-items: center; gap: 12px;
    font-weight: 900; font-size: 34px; letter-spacing: 0.5px;
  }
  .wordmark__dot {
    width: 22px; height: 22px; border-radius: 50%;
  }
  .card--back .wordmark { color: var(--card-white); }
  .card--back .wordmark__dot { background: var(--card-white); }

  .card--front { background: var(--card-white); }
  .card__wave { position: absolute; inset: 0; }
  .card--front .wordmark {
    position: absolute; top: 80px; right: 44px;
    color: var(--text-dark); font-size: 28px;
  }
  .card--front .wordmark__dot { background: var(--text-dark); }

  .person { position: absolute; left: 44px; top: 112px; }
  .person__name {
    font-weight: 900; font-size: 34px; color: var(--text-dark);
  }
  .person__surname { color: var(--brand-blue); }
  .person__role {
    margin-top: 4px; margin-left: 4px;
    font-size: 17px; color: var(--text-muted);
  }

  .contact {
    position: absolute; left: 210px; bottom: 24px;
    list-style: none; color: var(--text-light);
    font-size: 19px; line-height: 1;
  }
  .contact__item { display: flex; align-items: center; gap: 14px; margin-top: 10px; }
  .contact__icon { width: 18px; height: 18px; flex: none; }
</style>
</head>
<body>
<main class="sheet">
  <section class="card card--back" aria-label="Card back">
    <div class="wordmark"><span class="wordmark__dot"></span>Granite Trench Co</div>
  </section>

  <section class="card card--front" aria-label="Card front">
    <svg class="card__wave" viewBox="0 0 640 366" preserveAspectRatio="none" aria-hidden="true">
      <path d="M90,366 C100,290 170,224 400,218 C540,214 612,170 640,70 L640,366 Z" fill="var(--card-black)"/>
      <path d="M68,366 C78,280 160,208 420,203" fill="none" stroke="var(--brand-blue)" stroke-width="7"/>
    </svg>

    <div class="wordmark"><span class="wordmark__dot"></span>Granite Trench Co</div>

    <div class="person">
      <h1 class="person__name">Dale <span class="person__surname">Whitcombe</span></h1>
      <p class="person__role">Owner</p>
    </div>

    <ul class="contact">
      <li class="contact__item">
        <svg class="contact__icon" viewBox="0 0 24 24" aria-hidden="true"><path fill="#fff" d="M6.6 10.8a15 15 0 0 0 6.6 6.6l2.2-2.2c.3-.3.7-.4 1-.2 1.1.4 2.3.6 3.6.6.6 0 1 .4 1 1V20c0 .6-.4 1-1 1A17 17 0 0 1 3 4c0-.6.4-1 1-1h3.5c.6 0 1 .4 1 1 0 1.3.2 2.5.6 3.6.1.3 0 .7-.2 1z"/></svg>
        604-555-0182
      </li>
      <li class="contact__item">
        <svg class="contact__icon" viewBox="0 0 24 24" aria-hidden="true"><path fill="#fff" d="M2 5h20v14H2z"/><path d="M2 5l10 8 10-8" fill="none" stroke="#0b0b0b" stroke-width="1.6"/></svg>
        dale@granitetrenchco.example
      </li>
      <li class="contact__item">
        <svg class="contact__icon" viewBox="0 0 24 24" aria-hidden="true"><g fill="none" stroke="#fff" stroke-width="1.8"><circle cx="12" cy="12" r="10"/><ellipse cx="12" cy="12" rx="4.5" ry="10"/><path d="M2 12h20"/></g></svg>
        www.granitetrenchco.example
      </li>
    </ul>
  </section>
</main>
</body>
</html>
```